Coastline Lending Depot brochure design

We need a B5 format brochure design aimed at retail and sophisticated investors. The aim is to give prospective investors a product overview. Our products are Australian property secured, capital protected, direct mortgages with high yields and low risk.
The final design should communicate confidence in superior performance investment strategies aimed at personal wealth achievemnets.
Updates
Project Deadline Extended
Reason: We are extending the deadline as we had problems with attaching the text, logo & colour files.
Target Market(s)
Retail and sophisticated investors
Industry/Entity Type
Investment
Requirements
Must have
- We envisage the brochure to have 8 B5 pages, include company logo, and use corportae colour scheme. The text for the brochure is attached as well as company logo and corporate colour scheme.
Nice to have
- At designer's discretion.

```html
<!DOCTYPE html>
<html lang="en">
<head>
<meta charset="utf-8">
<title>Coastline Lending Depot – Brochure Spread</title>
<link href="https://fonts.googleapis.com/css2?family=Didact+Gothic&display=swap" rel="stylesheet">
<style>
  :root {
    --navy: #1d3566;
    --ink: #1f3a70;
    --accent: #f26a21;
    --paper: #ffffff;
  }
  * { margin: 0; padding: 0; box-sizing: border-box; }
  html, body { width: 1200px; height: 853px; overflow: hidden; background: var(--paper); }
  body {
    position: relative;
    font-family: "Didact Gothic", "Century Gothic", sans-serif;
    color: var(--ink);
    font-size: 11.6px;
    line-height: 15.2px;
  }
  .spread {
    position: absolute; inset: 0;
    border: 1.5px solid var(--navy);
    border-radius: 0 0 6px 6px;
  }
  .tab {
    position: absolute;
    height: 30px;
    background: var(--navy);
    color: var(--accent);
    text-transform: uppercase;
    font-size: 12.5px;
    letter-spacing: -0.2px;
    line-height: 30px;
    text-align: center;
    border-radius: 12px 12px 12px 0;
  }
  .tab--left { left: 0; width: 342px; border-radius: 0 12px 12px 0; }
  .tab--right { left: 598px; width: 342px; border-radius: 12px 12px 12px 0; }
  .copy {
    position: absolute;
    text-align: justify;
    text-indent: 24px;
  }
  .copy--left { left: 12px; width: 578px; }
  .copy--right { left: 612px; width: 574px; }
  .list { position: absolute; left: 38px; list-style: none; }
  .list li::before { content: "» "; color: var(--accent); }
  .list--deep { left: 58px; width: 540px; }
  .hl { color: var(--accent); }
  .choice { position: absolute; left: 40px; }
  .page-no {
    position: absolute; bottom: 0;
    width: 14px; height: 15px;
    background: var(--navy);
    color: var(--accent);
    font-size: 10px; line-height: 15px; text-align: center;
  }
  .page-no--left { left: 0; }
  .page-no--right { right: 0; }
</style>
</head>
<body>
<div class="spread"></div>

<!-- Page 4 -->
<div class="tab tab--left" style="top:58px">Product Overview</div>
<p class="copy copy--left" style="top:121px">All loan applications go through a rigorous 20 point underwriting check, are professionaly inspected and valued (your mortgage will be a maximum of 75% of the secured property value), and then be properly secured by a registered mortgage against a property by Harbourline Legal, a national fully licensed and insured solicitor firm.</p>
<ul class="list" style="top:202px">
  <li>Minimum individual amounts: AUD$ 50,000</li>
  <li>Maximum individual loan amounts: AUD$ 500,000</li>
  <li>Average Loan to Value Ratio (LVR): 60%</li>
  <li>Maximum Loan to Value Ratio (LVR): 75%</li>
  <li>Choice of 3 - 12 months loan term</li>
</ul>

<div class="tab tab--left" style="top:353px">Liquidity</div>
<p class="copy copy--left" style="top:421px">This opportunity introduces liquidity to private direct mortgages and combines that with credit on hancement to alleviate problems for individual investors and Self Managed Super Funds, primarily lack of liquidity, unacceptable/unquantifiable risk and lack of professional management.</p>
<ul class="list" style="top:488px">
  <li>Target Investment Term: › 24 months</li>
  <li>Minimum Investment Term: 12 months</li>
  <li>Redemption is by 90 days written notice (subject to a minimum period of 12 months)</li>
</ul>

<div class="tab tab--left" style="top:597px">Investor Returns</div>
<p class="copy copy--left" style="top:668px">Investing in direct mortgages will get you several steps ahead of everyone else in terms of investment returns. Our investors Return On Investment (ROI) is a minimum of 10% p.a.</p>
<p class="choice" style="top:707px">Choice of:</p>
<ul class="list list--deep" style="top:726px">
  <li><span class="hl">Settlement Fund,</span> interest payments are paid to the “Lender” quarterly in arrears on the (15th day of December, March, June and September.</li>
  <li><span class="hl">Settled Loans,</span> pay interest up front for the particular mortgage at the specified loan rate.</li>
</ul>

<!-- Page 5 -->
<div class="tab tab--right" style="top:58px">What Risks Are Involved?</div>
<p class="copy copy--right" style="top:139px">A Capital Protected Investment is a type of asset backed security that is secured by registered 1st and 2nd mortgage over Australian property. Wgen you invest in a capital protected direct mortgage you are essentially lending money to a property owner for business purposes while securing your money by taking a mortgage on the property just like a bank does. This model of investment has proven to be one of the most safe and profitable investment strategies when done correctly, and that’s mainly why banks fight for a piece of the mortgage market.</p>
<p class="copy copy--right" style="top:278px">Investing (as lender) in direct mortgages is a popular choice for many private investors and self managed super funds (SMSF) seeking safe, premium returns alternative investments to cash or fixed interest bonds. You get the added security of property security, and a irondad default twenty one day buy back guarantee, which means that in case of a default, your mortgage will be bought back by the manager without questions.</p>
<p class="copy copy--right" style="top:402px">A Capital Protected Investment is a type of asset backed security that is secured by registered 1st and 2nd mortgage over Australian property. Wgen you invest in a capital protected direct mortgage you are essentially lending money to a property owner for business purposes while securing your money by taking a mortgage on the property just like a bank does. This model of investment has proven to be one of the most safe and profitable investment strategies when done correctly, and that’s mainly why banks fight for a piece of the mortgage market.</p>
<p class="copy copy--right" style="top:541px">Investing (as lender) in direct mortgages is a popular choice for many private investors and self managed super funds (SMSF) seeking safe, premium returns alternative investments to cash or fixed interest bonds. You get the added security of property security, and a irondad default twenty one day buy back guarantee, which means that in case of a default, your mortgage will be bought back by the manager without questions.</p>

<div class="page-no page-no--left">4</div>
<div class="page-no page-no--right">5</div>
</body>
</html>
```